Luxury Stationer Design company needs a web page

We need a web page for a new start up company that creates and or customizes all things stationery for events, businesses, and branding. We are a high end stationer company because our custom designs are very intricate and luxurious. Our products set the tone for the client and raises the bar for their event, presentation, or image. We would like to see a web page that exudes luxury but is very user friendly. We will require a home page, about page, Shop/Store page, Gallery, Our process, Contact Us, Terms of Use, Privacy Policy. Once a designer picks the project, we can further communicate about the content. For now just to get started, lets just use place holders for verbiage.The final design should communicate luxury, high-end, couture custom designs.

Target Market(s)

Brides, Event planners, corporate/commercial business, DIY brides,

Coding

Coded - Design and coding required

Font styles to use
Serif
Script

Colors

Designer to choose colors to be used in the design.

Requirements
Must have
• We will require a home page, about page, Shop/Store page, Gallery, Our process, Contact Us, Terms of Use, Privacy Policy.
Nice to have
• Frequency Asked Questions
• Consultation Appointment Book Page

```html
<!DOCTYPE html>
<html lang="en">
<head>
<meta charset="utf-8">
<title>Velloria – Custom Collections</title>
<link href="https://fonts.googleapis.com/css2?family=Raleway:wght@200;300;400&family=Lato:wght@300;400;700&family=Great+Vibes&display=swap" rel="stylesheet">
<style>
:root{
  --plum:#7b2a60;
  --plum-dark:#5b4a5d;
  --rose:#c5407d;
  --ink:#222;
  --muted:#777;
  --line:#ddd;
  --white:#fff;
  --blush:#f3e4f1;
}
*{margin:0;padding:0;box-sizing:border-box}
html,body{width:1200px;height:4826px;overflow:hidden}
body{font-family:'Lato',sans-serif;color:var(--ink);background:var(--white);position:relative}
.section{position:absolute;left:0;width:1200px}
.abs{position:absolute}
.center{left:0;width:1200px;text-align:center}
.heading{font-family:'Raleway',sans-serif;font-weight:200;font-size:44px;letter-spacing:3px;color:#444}
.rule{position:absolute;left:578px;width:44px;height:3px;background:var(--rose)}
.script{font-family:'Great Vibes',cursive}
.btn{position:absolute;background:var(--plum);color:#fff;font-size:12px;font-weight:700;letter-spacing:.5px;text-transform:uppercase;display:flex;align-items:center;justify-content:center}
.ph{position:absolute}

/* hero */
.hero{top:0;height:830px;background:linear-gradient(135deg,#a9a2a6,#8f878c 45%,#b5aaa9)}
.hero-shade{position:absolute;inset:0;background:rgba(40,30,40,.35)}
.util{top:48px;right:112px;color:#fff;font-size:13px;letter-spacing:.5px;display:flex;gap:16px}
.logo{font-family:'Raleway',sans-serif;font-weight:300;color:#fff;font-size:42px;letter-spacing:2px}
.nav{top:88px;left:436px;display:flex;gap:30px;color:#fff;font-size:15px}
.hero-title{top:320px;font-family:'Raleway',sans-serif;font-weight:200;font-size:104px;color:#fff;letter-spacing:6px}
.hero-script{top:450px;font-size:62px;color:#fff}
.hero-sub{top:552px;color:#fff;font-size:19px}
.dots{display:flex;gap:8px;justify-content:center}
.dots span{width:11px;height:11px;border-radius:50%;border:1.5px solid #fff}
.dots .on{background:#fff}

/* gallery */
.tile{position:absolute}
.logo-box{position:absolute;top:2104px;width:180px;height:103px;border:1px solid #ccc;background:#fff;display:flex;align-items:center;justify-content:center;font-family:'Raleway',sans-serif;font-size:22px;color:#444}

/* process */
.process{top:2310px;height:682px;background:linear-gradient(180deg,#5d4c5f,#4f4252)}
.step{position:absolute;top:2455px;width:200px;text-align:center;color:#fff}
.step .ring{width:112px;height:112px;border:2px solid #fff;border-radius:50%;margin:0 auto;display:flex;align-items:center;justify-content:center}
.step h3{font-weight:400;font-size:18px;margin-top:32px}
.step p{font-size:12px;line-height:22px;margin-top:12px;color:#eee}
.dash{position:absolute;top:2510px;width:110px;border-top:2px dotted #fff}

/* blog */
.post{position:absolute;top:3230px;width:302px}
.post .img{height:190px}
.post h4{font-weight:400;font-size:17px;line-height:26px;margin-top:30px;color:#222}
.post p{font-size:12px;line-height:22px;color:var(--muted);margin-top:16px}
.post a{display:block;font-size:12px;color:var(--plum);margin-top:18px;text-decoration:none}

/* testimonials */
.quote{top:3828px;height:586px;background:linear-gradient(90deg,#f4dcef,#f8eef6 50%,#f1d8ee)}

/* footer */
.footer{top:4414px;height:412px;background:#fff}
.foot-h{font-size:16px;font-weight:700;letter-spacing:1px}
.foot-list{font-size:13px;line-height:31px;color:#333}
.dot{width:18px;height:18px;border-radius:50%;background:#222;display:inline-block}
.card{width:40px;height:24px;border-radius:3px;display:inline-block}
</style>
</head>
<body>

<!-- Hero -->
<header class="section hero">
  <div class="ph" role="img" aria-label="Photo of a floral wedding invitation suite with pearls" style="inset:0;background:linear-gradient(135deg,#b7aeb2,#9a9196 50%,#c2b5b2)"></div>
  <div class="hero-shade"></div>
  <div class="abs util"><span>♥ FAVORITES</span><span>|</span><span>REGISTER</span><span>|</span><span>LOGIN</span><span>|</span><span>CART ( 0 )</span></div>
  <div class="abs logo" style="top:68px;left:112px">VELLORIA</div>
  <nav class="abs nav"><span>Home</span><span>About</span><span>Shop/Store</span><span>Gallery</span><span>Our process</span><span>Appointment</span><span>Contact Us</span></nav>
  <div class="abs center hero-title">VELLORIA</div>
  <div class="abs center script hero-script">Custom Collections</div>
  <div class="abs center hero-sub">Sed ut perspiciatis unde omnis iste natus error sit voluptatem</div>
  <div class="btn" style="top:618px;left:294px;width:298px;height:46px">Setup your custom consultation</div>
  <div class="btn" style="top:618px;left:609px;width:298px;height:46px;background:transparent;border:2px solid #fff">Get your custom invitation guide</div>
  <div class="abs center dots" style="top:760px"><span></span><span></span><span class="on"></span><span></span><span></span></div>
</header>

<!-- Creates -->
<section class="section" style="top:830px;height:1055px;background:linear-gradient(180deg,#fff,#faf6f9)">
  <div class="rule" style="top:98px"></div>
  <div class="abs center heading" style="top:105px">WE CREATES AND OR CUSTOMIZES</div>
  <div class="abs center script" style="top:163px;font-size:34px;color:#333">All things stationery for events, businesses, and branding.</div>
</section>
<div class="tile" role="img" aria-label="Gold laser-cut wedding invitation" style="top:1090px;left:113px;width:637px;height:297px;background:linear-gradient(135deg,#d8b53a,#e8e1d6)"></div>
<div class="tile" role="img" aria-label="Navy and gold art deco invitation" style="top:1090px;left:759px;width:328px;height:297px;background:linear-gradient(135deg,#2a2f7a,#b9a46a)"></div>
<div class="tile" role="img" aria-label="Burgundy floral invitation suite" style="top:1396px;left:113px;width:318px;height:290px;background:linear-gradient(135deg,#5a2233,#d9d1cf)"></div>
<div class="tile" role="img" aria-label="Maroon invitation box with card" style="top:1396px;left:441px;width:318px;height:290px;background:linear-gradient(135deg,#8b1d35,#e8e2e0)"></div>
<div class="tile" role="img" aria-label="Pink baby announcement cards" style="top:1396px;left:769px;width:318px;height:290px;background:linear-gradient(135deg,#f1d6e0,#cfa9b4)"></div>
<div class="btn" style="top:1741px;left:453px;width:294px;height:44px">Setup your custom consultation</div>

<!-- As seen on -->
<section class="section" style="top:1885px;height:425px;background:#f6f4f5">
  <div class="rule" style="top:92px"></div>
  <div class="abs center heading" style="top:100px">AS SEEN ON</div>
</section>
<div class="logo-box" style="left:113px">Vow Ledger</div>
<div class="logo-box" style="left:312px">Paper Rite</div>
<div class="logo-box" style="left:512px">Coral Press</div>
<div class="logo-box" style="left:708px">Petal Post</div>
<div class="logo-box" style="left:907px">Inkwell Daily</div>

<!-- Process -->
<section class="section process">
  <div class="rule" style="top:100px;background:#d0609a"></div>
  <div class="abs center heading" style="top:105px;color:#fff">THE PROCESS</div>
  <svg class="abs" style="top:240px;left:93px" width="20" height="30"><path d="M15 3 L4 15 L15 27" stroke="#fff" stroke-width="3" fill="none"/></svg>
  <svg class="abs" style="top:240px;left:1087px" width="20" height="30"><path d="M5 3 L16 15 L5 27" stroke="#fff" stroke-width="3" fill="none"/></svg>
</section>
<div class="dash" style="left:290px"></div><div class="dash" style="left:540px"></div><div class="dash" style="left:790px"></div>
<div class="step" style="left:124px"><div class="ring"><svg width="44" height="44" fill="none" stroke="#fff" stroke-width="2"><circle cx="22" cy="15" r="8"/><path d="M6 40c2-10 9-14 16-14s14 4 16 14"/></svg></div><h3>Consultation</h3><p>At the initial consultation, we discuss your project in great detail. This is when</p><p>⌄</p></div>
<div class="step" style="left:376px"><div class="ring"><svg width="44" height="44" fill="none" stroke="#fff" stroke-width="2"><path d="M6 10h32v20H18l-8 7v-7H6z"/></svg></div><h3>Quote</h3><p>After you approve the price with realize and agree to move forward with the process,</p><p>⌄</p></div>
<div class="step" style="left:624px"><div class="ring"><svg width="44" height="44" fill="none" stroke="#fff" stroke-width="2"><path d="M8 20h7v18H8zM15 22l8-14c4 0 4 4 3 8h10c2 0 3 2 2 4l-3 14c-1 2-2 3-4 3H15"/></svg></div><h3>Contract</h3><p>After the quote is accepted, a 50% deposit is required along with a signed contract.</p><p>⌄</p></div>
<div class="step" style="left:875px"><div class="ring"><svg width="44" height="44" fill="none" stroke="#fff" stroke-width="2"><rect x="5" y="8" width="34" height="22" rx="2"/><path d="M16 38h12M22 30v8"/></svg></div><h3>Design</h3><p>Once your contract and deposit is received, we immediately start on the first design draft.</p><p>⌄</p></div>
<div class="btn" style="top:2857px;left:512px;width:176px;height:44px">View process</div>

<!-- Blog -->
<section class="section" style="top:2992px;height:836px;background:linear-gradient(180deg,#faf8f3,#f7f5f6)">
  <div class="rule" style="top:104px"></div>
  <div class="abs center heading" style="top:110px">AS SEEN ON</div>
</section>
<article class="post" style="left:113px"><div class="img" role="img" aria-label="Laser-cut monogram invitation" style="background:linear-gradient(135deg,#8a5a4a,#d9b3a1)"></div><h4>Sed ut perspiciatis unde omnis iste natus error svoluptatem.</h4><p>At vero eos et accusamus et iusto odio dignissimos ducimus qui blanditiis voluptatum.</p><a>READ MORE</a></article>
<article class="post" style="left:450px"><div class="img" role="img" aria-label="Blue invitation with gold emblem" style="background:linear-gradient(135deg,#2c4f8f,#d8b64c)"></div><h4>Sed ut perspiciatis unde omnis iste natus error svoluptatem.</h4><p>At vero eos et accusamus et iusto odio dignissimos ducimus qui blanditiis voluptatum.</p><a>READ MORE</a></article>
<article class="post" style="left:785px"><div class="img" role="img" aria-label="Floral invitation suite with envelope" style="background:linear-gradient(135deg,#e8dcd6,#9b3448)"></div><h4>Sed ut perspiciatis unde omnis iste natus error svoluptatem.</h4><p>At vero eos et accusamus et iusto odio dignissimos ducimus qui blanditiis voluptatum.</p><a>READ MORE</a></article>
<div class="btn" style="top:3668px;left:512px;width:176px;height:44px">Explore the blog</div>

<!-- Testimonials -->
<section class="section quote">
  <div class="rule" style="top:82px"></div>
  <div class="abs center heading" style="top:90px">WHAT OUR CLIENTS ARE SAYING</div>
  <div class="ph" role="img" aria-label="Client portrait" style="top:196px;left:536px;width:128px;height:128px;border-radius:50%;background:linear-gradient(135deg,#c9b2a4,#6e7a92)"></div>
  <p class="abs center" style="top:362px;font-size:14px;line-height:32px;color:#444">At vero eos et accusamus et iusto odio dignissimos ducimus qui blanditiis praesentium voluptatum deleniti atque cor-<br>rupti quos dolores et quas molestias excepturi sint occaecati cupiditate non sunt in culpa qui officia deserunt est</p>
  <p class="abs center" style="top:432px;font-size:15px"><b style="color:var(--plum)">John Doe</b> <span style="color:#777;font-size:13px">Customer</span></p>
  <div class="abs center" style="top:478px;display:flex;gap:8px;justify-content:center"><span style="width:24px;height:24px;border-radius:50%;background:var(--rose);color:#fff;font-size:11px;display:flex;align-items:center;justify-content:center">1</span><span style="width:24px;height:24px;border-radius:50%;background:#fff;font-size:11px;display:flex;align-items:center;justify-content:center">2</span></div>
</section>

<!-- Footer -->
<footer class="section footer">
  <div class="abs" style="top:80px;left:113px;font-family:'Raleway',sans-serif;font-weight:300;font-size:46px;letter-spacing:2px">VELLORIA</div>
  <p class="abs" style="top:180px;left:113px;width:300px;font-size:12px;line-height:24px;color:#444">At vero eos et accusamus et iusto odio dignissimos ducimus qui blanditiis praesentium voluptatum deleniti atque corrupti quos dolores et.</p>
  <div class="abs foot-h" style="top:74px;left:528px">MAIN MENU</div>
  <div class="abs foot-list" style="top:108px;left:528px">Home<br>About<br>Shop/Store<br>Gallery<br>Our process</div>
  <div class="abs foot-list" style="top:108px;left:628px">Appointment<br>Contact Us</div>
  <div class="abs foot-h" style="top:74px;left:824px">SIGN UP TO NEWSLETTER</div>
  <div class="abs" style="top:116px;left:824px;width:170px;height:44px;border:1px solid #ccc;font-size:12px;color:#777;padding:14px 12px">Email Address</div>
  <div class="btn" style="top:116px;left:994px;width:90px;height:44px;text-transform:none;font-size:14px">Sign Up</div>
  <div class="abs foot-h" style="top:194px;left:824px">FOLLOW US</div>
  <div class="abs" style="top:230px;left:824px;display:flex;gap:14px"><span class="dot"></span><span class="dot"></span><span class="dot"></span><span class="dot"></span><span class="dot"></span></div>
  <div class="abs" style="top:340px;left:113px;width:974px;border-top:1px solid var(--line)"></div>
  <div class="abs" style="top:366px;left:113px;font-size:11px;color:#333">© 2018 Copyrights Velloria Studio All Rights Reserved &nbsp;|&nbsp; Terms of Use &nbsp;|&nbsp; Privacy Policy</div>
  <div class="abs" style="top:362px;left:922px;display:flex;gap:6px"><span class="card" style="background:#e0a030"></span><span class="card" style="background:#2a5bb0"></span><span class="card" style="background:#3a86c8"></span><span class="card" style="background:#c8c8c8"></span></div>
</footer>

</body>
</html>
```